Professional Law Firm Rebranding Brochure Layout Design

Our law firm is changing its name from The Law Office of Dana Moreno, PLLC to MORENO.LAW. I would like a 4-page color brochure (cover, page 2, page 3, back) that announces and explains our rebranding. I have attached lots of files that should be helpful. I envision the words "The Law Office of Dana Moreno, PLLC is now known as MORENO.LAW" at the top of the front cover. Feel free to review our website at https://moreno-legal.example to get an idea of the look and feel we like. Tall buildings and other professional images work well.

Target Market(s)

Businesses, law firm clients, entrepreneurs, startups, corporations

Industry/Entity Type

Legal

Font styles to use
Sans Serif

Colors
cfdeed
85abd2
3276b5
0555a3
cee9f5
85cae6
33a6d7
0492cd

Requirements
Must have
• Professional appearance, photos & bios of team members, explanation of rebranding - finished product is US letter size

```html
<!DOCTYPE html>
<html lang="en">
<head>
<meta charset="utf-8">
<title>MORENO.LAW – Rebranding Brochure</title>
<link href="https://fonts.googleapis.com/css2?family=Montserrat:wght@300;400;500;600;700&display=swap" rel="stylesheet">
<style>
  :root {
    --gold: #c6ae6e;
    --blue: #1273b9;
    --ink: #111111;
    --white: #ffffff;
    --glass-1: #56718f;
    --glass-2: #2e4763;
    --glass-3: #1b2c40;
  }
  * { margin: 0; padding: 0; box-sizing: border-box; }
  html, body { width: 1200px; height: 850px; overflow: hidden; background: #ffffff; }
  body { font-family: "Montserrat", sans-serif; }

  .spread { position: relative; width: 1200px; height: 850px; overflow: hidden; }

  .photo-backdrop {
    position: absolute; inset: 0;
    background:
      radial-gradient(ellipse at 75% 45%, #7fa3c9 0%, rgba(127,163,201,0) 45%),
      linear-gradient(160deg, var(--glass-1) 0%, var(--glass-2) 45%, var(--glass-3) 100%);
  }
  .chevron-art { position: absolute; inset: 0; width: 1200px; height: 850px; }
  .fold { position: absolute; left: 600px; top: 0; width: 1px; height: 850px; background: rgba(255,255,255,0.35); }

  /* Inside flap (left) */
  .flap-title { position: absolute; right: 657px; top: 42px; text-align: right; white-space: nowrap; }
  .flap-title .former { font-size: 21.5px; font-weight: 500; color: var(--ink); letter-spacing: 0.2px; }
  .flap-title .transition { font-size: 21.5px; font-weight: 500; color: var(--gold); margin-top: 6px; }
  .flap-title .new-name { font-size: 55px; font-weight: 500; color: var(--blue); line-height: 1; margin-top: 4px; letter-spacing: 0.5px; }

  .mission-card {
    position: absolute; left: 328px; top: 178px; width: 219px; height: 232px;
    background: var(--gold); border-radius: 14px; padding: 20px 14px 0 22px;
    color: var(--white); font-size: 12.3px; font-weight: 600; line-height: 1.35;
  }
  .url-pill {
    position: absolute; height: 26px; border-radius: 13px; white-space: nowrap;
    font-size: 12px; font-weight: 500; display: flex; align-items: center; justify-content: center;
  }
  .url-pill.personal { left: 345px; top: 408px; width: 184px; background: var(--white); border: 2px solid var(--blue); color: var(--ink); font-size: 11.5px; }

  .intro { position: absolute; left: 83px; top: 230px; width: 232px; color: var(--white); font-size: 12.2px; line-height: 1.3; font-weight: 500; }
  .intro .lead { font-size: 16.5px; font-weight: 700; color: var(--gold); }
  .intro p + p { margin-top: 14px; }

  .rule { position: absolute; height: 1.5px; background: rgba(255,255,255,0.8); }
  .invite { position: absolute; left: 83px; top: 634px; width: 245px; color: var(--white); font-size: 12.2px; font-weight: 700; line-height: 1.3; }
  .invite .phone { color: var(--gold); white-space: nowrap; }

  .wordmark { position: absolute; left: 81px; top: 748px; display: flex; align-items: center; gap: 8px; }
  .wordmark .mark-square { width: 34px; height: 34px; background: var(--white); }
  .wordmark .mark-name { font-size: 27px; font-weight: 700; color: var(--white); letter-spacing: 0.3px; }

  .locations { position: absolute; left: 369px; top: 624px; color: var(--white); font-size: 12.2px; font-weight: 700; line-height: 1.3; }
  .locations h3 { font-size: 14px; font-weight: 600; color: var(--gold); letter-spacing: 0.5px; }
  .locations .office { margin-top: 8px; }
  .locations .office + .office { margin-top: 14px; }

  /* Front cover (right) */
  .cover-title { position: absolute; left: 641px; top: 66px; white-space: nowrap; }
  .cover-title .former { font-size: 22.5px; font-weight: 500; color: var(--ink); letter-spacing: 0.2px; }
  .cover-title .transition { font-size: 28px; font-weight: 500; color: var(--gold); margin-top: 10px; }
  .cover-title .new-name { font-size: 68px; font-weight: 500; color: var(--blue); line-height: 1; margin-top: 4px; letter-spacing: 0.5px; }

  .tagline { position: absolute; right: 48px; top: 584px; text-align: right; font-size: 55px; line-height: 0.98; letter-spacing: 0.5px; white-space: nowrap; }
  .tagline .solutions { color: var(--gold); font-weight: 500; }
  .tagline .growing { color: var(--white); font-weight: 300; }
  .tagline .businesses { color: var(--white); font-weight: 600; }

  .url-pill.firm { left: 966px; top: 781px; width: 188px; background: var(--gold); border: 2px solid var(--blue); color: var(--ink); font-size: 12px; }
</style>
</head>
<body>
<main class="spread">
  <div class="photo-backdrop" role="img" aria-label="Looking up at glass skyscrapers against a blue sky with clouds"></div>

  <svg class="chevron-art" viewBox="0 0 1200 850" aria-hidden="true">
    <defs>
      <linearGradient id="sky" x1="0" y1="0" x2="0" y2="1">
        <stop offset="0" stop-color="#eef4fa"/>
        <stop offset="0.6" stop-color="#f7f9fc"/>
        <stop offset="1" stop-color="#dfe9f4"/>
      </linearGradient>
    </defs>
    <polygon points="0,0 1200,0 1200,240 718,376 0,102" fill="url(#sky)"/>
    <polygon points="0,96 718,370 1200,234 1200,252 718,388 0,116" fill="var(--gold)"/>
  </svg>

  <div class="fold"></div>

  <!-- Inside flap -->
  <header class="flap-title">
    <div class="former">THE LAW OFFICE OF DANA MORENO, PLLC</div>
    <div class="transition">IS NOW KNOWN AS</div>
    <div class="new-name">MORENO.LAW</div>
  </header>

  <section class="mission-card">
    MORENO.LAW’s goal is to enrich and empower our clients by providing high quality work product and creative legal solutions to their legal problems. One way we achieve this goal is by leveraging technology and utilizing data to improve the efficiency and effectiveness of our services.
  </section>
  <div class="url-pill personal">www.danamoreno.example</div>

  <section class="intro">
    <p><span class="lead">At MORENO.LAW,</span><br>we strive to help our clients avoid costly legal mistakes. Preventing legal problems is always cheaper and easier than dealing with them after they occur, which is why our attorneys and staff pride themselves on anticipating clients’ needs and meeting them.</p>
    <p>Our primary areas of practice are business and intellectual property law. Our firm’s clients range from entrepreneurs and startup companies to multi-national corporations. We understand that regardless of where your company may be in its life cycle, legal decisions are business decisions. Your strategic business objectives always factor into our legal advice.</p>
  </section>

  <div class="rule" style="left:83px; top:619px; width:46px;"></div>
  <section class="invite">
    We would welcome the opportunity to earn a place as your reliable trusted advisor. To learn more about MORENO.LAW, please contact us at info@moreno-legal.example or <span class="phone">555-014-2290.</span>
  </section>

  <div class="wordmark">
    <span class="mark-square"></span>
    <span class="mark-name">MORENO.LAW</span>
  </div>

  <section class="locations">
    <h3>LOCATIONS</h3>
    <div class="rule" style="left:0; top:26px; width:46px;"></div>
    <div class="office" style="margin-top:18px;">Charlotte Office<br>480 Harbor Point Avenue,<br>Suite 200<br>Charlotte, NC 28299</div>
    <div class="office">Davidson Office<br>75 Maple Mill Road<br>Davidson, NC 28099</div>
  </section>

  <!-- Front cover -->
  <header class="cover-title">
    <div class="former">THE LAW OFFICE OF DANA MORENO, PLLC</div>
    <div class="transition">IS NOW KNOWN AS</div>
    <div class="new-name">MORENO.LAW</div>
  </header>

  <h2 class="tagline">
    <span class="solutions">SOLUTIONS</span><br>
    <span class="growing">FOR GROWING</span><br>
    <span class="businesses">BUSINESSES</span>
  </h2>

  <div class="rule" style="left:1048px; top:760px; width:104px;"></div>
  <div class="url-pill firm">www.moreno-legal.example</div>
</main>
</body>
</html>
```